Mobile phone battery need a packaging design.

We need a very special package for our mobile battery.Our product are of the best quality and long using . We mainly export to African countries. The package should be open window or something else, This package need to be able to see the battery directly from the outside package. And we will also have free pen in the packaging. We want our product to be special in shape or design in the market,So as to attract customer's attention. Use as bright shining colors as possible,This will get their attention. Design the battery label with package together, both different sides of the package.and also design the warranty card or service card we use to put inside the package or writing at backside of the package. Words on the package should also be designed by design( Advertising language) The color of our company is green , but if you have a more suitable color, we are willing to try . Thank u Attached is the battery sample photo and the pen sample

Colors

Designer to choose colors to be used in the design.

Requirements
Must have
• 1, Our package is that we must open the window to see the battery inside,
• 2, The packaging has to be special, different from the market packaging,need fashionable.
• 3, We need your designers to design the advertising language and promotion language of our products,and to match the packaging.

```html
<!DOCTYPE html>
<html lang="en">
<head>
<meta charset="utf-8">
<title>Voltara Battery Packaging</title>
<link rel="stylesheet" href="https://fonts.googleapis.com/css2?family=Titillium+Web:ital,wght@0,300;0,400;0,600;0,700;0,900;1,600&display=swap">
<style>
  :root {
    --page: #ffffff;
    --panel: #050805;
    --panel-edge: #1a1d1a;
    --green: #0bb04a;
    --green-bright: #2dff7a;
    --green-deep: #06421d;
    --white: #ffffff;
    --grey: #cfd3cf;
  }
  * { margin: 0; padding: 0; box-sizing: border-box; }
  html, body { width: 1200px; height: 1200px; overflow: hidden; background: var(--page); }
  body { position: relative; font-family: "Titillium Web", sans-serif; color: var(--white); }

  .box-front {
    position: absolute; left: 108px; top: 140px; width: 545px; height: 948px;
    background: var(--panel); overflow: hidden;
  }
  .brand-name {
    position: absolute; left: 0; right: 0; top: 58px; text-align: center;
    font-weight: 700; font-size: 62px; letter-spacing: 3px; color: var(--green);
  }
  .brand-name .brand-dot {
    display: inline-block; width: 18px; height: 18px; background: var(--green);
    margin-left: 12px; vertical-align: middle;
  }
  .tagline {
    position: absolute; left: 67px; top: 160px; width: 361px; height: 49px;
    display: flex; border: 2px solid var(--green);
  }
  .tagline-strong {
    background: var(--green); color: var(--white); font-weight: 700; font-size: 24px;
    width: 155px; display: flex; align-items: center; justify-content: center;
  }
  .tagline-light {
    flex: 1; color: var(--green); font-weight: 300; font-size: 24px;
    display: flex; align-items: center; justify-content: center;
  }

  .gift-badge {
    position: absolute; left: -50px; top: 428px; width: 150px; height: 150px;
    border-radius: 50%; background: var(--green);
  }
  .gift-label {
    position: absolute; left: 48px; top: 580px; transform: rotate(-90deg); transform-origin: left top;
    font-weight: 900; font-size: 24px; letter-spacing: 0.5px; color: var(--white); white-space: nowrap;
  }
  .gift-pen {
    position: absolute; left: 38px; top: 250px; width: 28px; height: 430px;
    border-radius: 14px 14px 6px 6px; transform: rotate(5deg);
    background: linear-gradient(180deg, #8a2ca8 0%, #1c1c22 12%, #2a2a30 75%, #a0309e 100%);
  }

  .window {
    position: absolute; left: 133px; top: 252px; width: 270px; height: 414px;
    border: 3px solid var(--green); border-radius: 12px; background: var(--white); padding: 22px 18px;
  }
  .window .battery-mini {
    width: 100%; height: 100%; background: var(--panel); border-radius: 4px; position: relative; overflow: hidden;
  }
  .battery-mini .brand-name { font-size: 26px; top: 44px; letter-spacing: 1px; }
  .battery-mini .brand-name .brand-dot { width: 8px; height: 8px; margin-left: 6px; }
  .battery-mini .circuit { top: 150px; height: 160px; }

  .circuit {
    position: absolute; left: 0; right: 0;
    background:
      radial-gradient(ellipse 40% 45% at 40% 40%, rgba(45,255,122,0.75), rgba(11,176,74,0.25) 55%, transparent 80%),
      linear-gradient(180deg, transparent, var(--green-deep) 30%, #0a5a28 60%, transparent);
  }
  .box-front > .circuit { top: 595px; height: 275px; }

  .id-box {
    position: absolute; border: 1px solid var(--green); border-radius: 3px;
    font-size: 7px; color: var(--green); padding: 2px 5px; letter-spacing: 0.5px;
  }
  .box-front > .id-box { left: 80px; top: 880px; width: 172px; height: 48px; }
  .battery-mini .id-box { left: 8px; top: 318px; width: 95px; height: 24px; font-size: 5px; }

  .maker {
    position: absolute; left: 270px; top: 898px; font-style: italic; font-weight: 600;
    font-size: 17px; color: var(--white); white-space: nowrap;
  }

  .battery-label {
    position: absolute; left: 706px; top: 394px; width: 370px; height: 542px;
    background: var(--panel); border-radius: 4px 4px 12px 12px; overflow: hidden;
    border-top: 4px solid var(--panel-edge); border-bottom: 12px solid #262826;
  }
  .battery-label .brand-name { top: 68px; font-size: 42px; letter-spacing: 2px; }
  .battery-label .brand-name .brand-dot { width: 12px; height: 12px; margin-left: 8px; }
  .model {
    position: absolute; left: 0; right: 0; top: 186px; text-align: center;
    font-size: 21px; font-weight: 400; color: var(--white);
  }
  .model strong { font-weight: 700; }
  .battery-label .circuit { top: 245px; height: 220px; }
  .battery-label .id-box { left: 12px; top: 468px; width: 155px; height: 34px; font-size: 6px; }
  .origin {
    position: absolute; left: 222px; top: 478px; font-size: 12px; font-weight: 400; color: var(--white);
  }
</style>
</head>
<body>

<section class="box-front">
  <div class="brand-name">VOLTARA<span class="brand-dot"></span></div>
  <div class="tagline">
    <span class="tagline-strong">Rechargeable</span>
    <span class="tagline-light">Li-Polymer Battery</span>
  </div>

  <div class="circuit" role="img" aria-label="Glowing green circuit-board line pattern"></div>

  <div class="gift-badge"></div>
  <div class="gift-pen" role="img" aria-label="Black and purple ballpoint gift pen"></div>
  <div class="gift-label">GIFT PEN INSIDE</div>

  <div class="window">
    <div class="battery-mini">
      <div class="brand-name">VOLTARA<span class="brand-dot"></span></div>
      <div class="circuit" role="img" aria-label="Glowing green circuit-board line pattern"></div>
      <div class="id-box">ID SECTOR</div>
    </div>
  </div>

  <div class="id-box">CELL ID SECTOR</div>
  <div class="maker">Meridian Cell Works Co., LTD.</div>
</section>

<section class="battery-label">
  <div class="brand-name">VOLTARA<span class="brand-dot"></span></div>
  <div class="model">Model: <strong>VX-26A</strong></div>
  <div class="circuit" role="img" aria-label="Glowing green circuit-board line pattern"></div>
  <div class="id-box">ID SECTOR</div>
  <div class="origin">MADE IN CHINA</div>
</section>

</body>
</html>
```